Letterhead for Law Firm - Logo already prepared

I previously used to prepare a logo which I was quite pleased with, a copy is attached for your reference. I would like the font of the logo to be all the same size, rather than the 'S' and 'L' being larger than the other letters.
I have copies of the attached in other formats if necessary.
I need a letterhead prepared which is virtually identical to the draft attached, however I will be adding an address, phone number, fax number, mobile number and email. I will provide these details with whoever can assist me.
I will also be providing insurance details to be listed at the foot of the page.
Finally, I need the file to be supplied as a high resolution pdf with 2mm bleed.
If you require any further information, please do not hesitate to contact me.

```html
<!DOCTYPE html>
<html lang="en">
<head>
<meta charset="utf-8">
<title>Vantrell Legal – Letterhead</title>
<link href="https://fonts.googleapis.com/css2?family=Questrial&display=swap" rel="stylesheet">
<style>
  :root {
    --ink-grey: #6b6c70;
    --text-dark: #3a3a3c;
    --orange: #f26a21;
    --orange-light: #f7a14a;
    --paper: #ffffff;
    --mark-tint: #f7d8c6;
  }
  * { margin: 0; padding: 0; box-sizing: border-box; }
  html, body { width: 940px; height: 1200px; overflow: hidden; background: var(--paper); }
  .letterhead {
    position: relative;
    width: 940px;
    height: 1200px;
    background: var(--paper);
    font-family: "Questrial", sans-serif;
    overflow: hidden;
  }
  .brand {
    position: absolute;
    top: 14px;
    left: 52px;
    display: flex;
    align-items: center;
    gap: 26px;
  }
  .brand-dot {
    width: 118px;
    height: 118px;
    border-radius: 50%;
    background: var(--orange);
  }
  .brand-name {
    font-size: 64px;
    color: var(--ink-grey);
    letter-spacing: 0.5px;
    white-space: nowrap;
  }
  .watermark {
    position: absolute;
    left: 110px;
    top: 190px;
    width: 720px;
    height: 720px;
    border-radius: 50%;
    background: radial-gradient(circle at 50% 50%, #fdf3ec 0%, #fbe6d8 62%, var(--mark-tint) 70%, #fdf1e9 76%, rgba(255,255,255,0) 80%);
  }
  .contacts {
    position: absolute;
    left: 46px;
    top: 990px;
    list-style: none;
    display: flex;
    flex-direction: column;
    gap: 24px;
    z-index: 2;
  }
  .contact {
    display: flex;
    align-items: center;
    gap: 20px;
    font-size: 23px;
    line-height: 32px;
    color: var(--text-dark);
    white-space: nowrap;
  }
  .contact-icon {
    width: 42px;
    height: 32px;
    border-radius: 7px;
    background: var(--orange);
    display: flex;
    align-items: center;
    justify-content: center;
    flex: none;
  }
  .contact-icon svg { display: block; }
  .www-label { font-size: 12px; line-height: 1; color: var(--paper); letter-spacing: 0.5px; }
  .footer-swoosh {
    position: absolute;
    left: 0;
    bottom: 0;
    width: 940px;
    height: 110px;
    z-index: 1;
  }
</style>
</head>
<body>
<main class="letterhead">
  <header class="brand">
    <span class="brand-dot"></span>
    <span class="brand-name">Vantrell Legal</span>
  </header>

  <div class="watermark" role="img" aria-label="Large faint brand emblem watermark"></div>

  <ul class="contacts">
    <li class="contact">
      <span class="contact-icon">
        <svg width="26" height="20" viewBox="0 0 26 20" aria-hidden="true">
          <path d="M2 7c0-3 5-5 11-5s11 2 11 5v2h-6V6.5c-1.5-.6-3.2-.9-5-.9s-3.5.3-5 .9V9H2z" fill="#fff"/>
          <rect x="6" y="11" width="14" height="7" rx="2" fill="#fff"/>
        </svg>
      </span>
      <span>98-5120-3377</span>
    </li>
    <li class="contact">
      <span class="contact-icon"><span class="www-label">www</span></span>
      <span>www.vantrelllegal.com</span>
    </li>
    <li class="contact">
      <span class="contact-icon"></span>
      <span>socialhub.com/pages/vantrelllegal</span>
    </li>
  </ul>

  <svg class="footer-swoosh" viewBox="0 0 940 110" preserveAspectRatio="none" aria-hidden="true">
    <defs>
      <linearGradient id="swooshFill" x1="0" y1="0" x2="1" y2="0">
        <stop offset="0" stop-color="#f7a14a"/>
        <stop offset="0.5" stop-color="#f58a2e"/>
        <stop offset="1" stop-color="#f26a21"/>
      </linearGradient>
    </defs>
    <path d="M0 102 C 450 100, 720 80, 940 6 L940 110 L0 110 Z" fill="url(#swooshFill)"/>
    <path d="M0 108 C 450 106, 740 88, 940 30" fill="none" stroke="#fff" stroke-width="3" opacity="0.55"/>
  </svg>
</main>
</body>
</html>
```